Illustrationen für ein Balance Boards
Zielgruppe
Meine Firma verkauft Balance Boards und Skateboards.
Ich habe meine Balance Board Designs von meinen anderen 2 Produkten verlinkt.
Ich verlinke hier einmal meine Produkte und dabei wird die Zielgruppe deutlich klarer anhand der Bewertungen usw.
1. https://www.kaufwelt-beispiel.de/dp/Q71TRM5XWA?ref=myi_title_dp
2. https://www.kaufwelt-beispiel.de/dp/Q71JNH4ZRE?ref=myi_title_dp
Es soll dabei ein neues Design erstellt werden für das Board, welches auf dem Karton liegt.
Es wäre dabei gut, wenn das Bild 3D gerendert wird oder einfach das Bild von der Konkurrenz verwendet wird.
Das ist nicht das gleiche Board, aber relativ ähnlich.
Aufgabenstellung
Wichtig beim Design ist das es leicht sein soll neue Varianten zu erstellen indem man einfach die Farbe verändert. Das sieht man anhand von meinen anderen Produkten.
Das Logo war zudem immer sehr dominant auf meinen Produkten, aber ich bin bereit neue Optionen zusehen.

```html
<!DOCTYPE html>
<html lang="de">
<head>
<meta charset="utf-8">
<title>Balance Board Grafik</title>
<style>
  :root {
    --ink: #000000;
    --coral: #ff6161;
    --slate: #676767;
    --white: #ffffff;
    --dot-tone: #3c3c3c;
    --stripe-tone: #6e6e6e;
  }
  html, body {
    margin: 0;
    padding: 0;
    width: 1200px;
    height: 285px;
    overflow: hidden;
    background: var(--ink);
  }
  .board-art {
    display: block;
    width: 1200px;
    height: 285px;
  }
  .field { fill: var(--ink); }
  .sun-large, .sun-small { fill: var(--coral); }
  .moon-grey { fill: var(--slate); }
  .dot-field { fill: var(--dot-tone); }
  .stripe-band { fill: var(--stripe-tone); }
  .cross { fill: var(--white); }
</style>
</head>
<body>
<svg class="board-art" viewBox="0 0 1200 285" xmlns="http://www.w3.org/2000/svg">
  <defs>
    <linearGradient id="mesh-glow" x1="0" y1="0" x2="1" y2="0">
      <stop offset="0" stop-color="#ffffff" stop-opacity="0"/>
      <stop offset="0.25" stop-color="#ffffff" stop-opacity="0.14"/>
      <stop offset="0.6" stop-color="#ffffff" stop-opacity="0.18"/>
      <stop offset="1" stop-color="#ffffff" stop-opacity="0"/>
    </linearGradient>
  </defs>

  <rect class="field" x="0" y="0" width="1200" height="285"/>

  <rect class="stripe-band" x="0" y="0" width="316" height="42"
        role="img" aria-label="Fläche mit diagonalem weißem Streifenmuster"/>

  <circle class="dot-field" cx="128" cy="180" r="92"
          role="img" aria-label="Kreisfläche mit weißem Punktraster"/>

  <circle class="sun-large" cx="309" cy="146" r="165"/>

  <ellipse class="dot-field" cx="610" cy="285" rx="100" ry="52"
           role="img" aria-label="Halbkreis mit weißem Punktraster"/>

  <circle class="moon-grey" cx="743" cy="300" r="90"/>

  <rect x="212" y="0" width="724" height="285" fill="url(#mesh-glow)"
        role="img" aria-label="Geschwungenes Band aus feinen weißen Wellenlinien"/>

  <circle class="sun-small" cx="904" cy="141" r="26"/>

  <g class="cross" transform="translate(1063 134) rotate(45)">
    <rect x="-83" y="-14" width="166" height="28"/>
    <rect x="-14" y="-83" width="28" height="166"/>
  </g>
</svg>
</body>
</html>
```